Vantor Glide - Stock Certificate

We need a custom designed stock certificate that represents the look of our company logo but also have a cool look compared to a standard stock certificate. We thinking we want the logo in gold. Our website is https://www.vantorglideusa.example.

We are wanting the certificate to look very professional and really cool, we have sales agents that work for the company and we are creating a program by which the sales agents can gain ownership in the company. So the certificates need to have a very cool appeal and that provides a sense of pride in owning "Units" in Vantor Glide.
Updates

Reason: Extending so other board members can vote as well, thank you all!

Target Market(s)

Stock/Shareholders

Industry/Entity Type

It Company

Font styles to use
Script

Requirements
Must have
• Must look like a stock certificate, must use our logo which the psd file for it was attached.
Nice to have
• Nice to have the logo in gold

```html
<!DOCTYPE html>
<html lang="en">
<head>
<meta charset="utf-8">
<title>Vantor Glide — Unit Certificate</title>
<link rel="stylesheet" href="https://fonts.googleapis.com/css2?family=Montserrat:wght@500;600;700&family=Kaushan+Script&display=swap">
<style>
  :root {
    --ink: #0b0b0b;
    --ink-soft: #1c1c1c;
    --white: #ffffff;
    --gold: #e6c88a;
    --gold-deep: #c2924a;
    --gold-light: #f6e2b2;
    --band: #939393;
    --label: #1e1e1e;
  }
  * { box-sizing: border-box; margin: 0; padding: 0; }
  html, body { width: 1200px; height: 857px; overflow: hidden; background: var(--ink); }
  .certificate {
    position: relative;
    width: 1200px;
    height: 857px;
    background: var(--ink);
    overflow: hidden;
    font-family: "Montserrat", sans-serif;
  }
  .wave-texture {
    position: absolute;
    left: 22px; right: 22px; top: 0; bottom: 0;
    background:
      radial-gradient(ellipse at 30% 30%, rgba(40,40,40,0.9), transparent 60%),
      radial-gradient(ellipse at 75% 60%, rgba(36,36,36,0.85), transparent 55%),
      linear-gradient(160deg, var(--ink-soft), var(--ink) 70%);
  }
  .gold-edge {
    position: absolute;
    top: 0; bottom: 0;
    width: 22px;
    background: linear-gradient(180deg, var(--gold-deep) 0%, var(--gold-light) 40%, var(--gold-deep) 70%, var(--gold-light) 100%);
  }
  .gold-edge--left { left: 0; }
  .gold-edge--right { right: 0; }

  .cert-number {
    position: absolute;
    top: 34px; left: 60px;
    font-weight: 600;
    font-size: 14px;
    letter-spacing: 1.5px;
    color: var(--gold);
  }
  .unit-count {
    position: absolute;
    top: 34px; right: 60px;
    font-weight: 600;
    font-size: 14px;
    letter-spacing: 1.5px;
    color: var(--gold);
    text-align: right;
  }

  .brand {
    position: absolute;
    top: 268px;
    left: 0; right: 0;
    display: flex;
    justify-content: center;
    align-items: center;
    gap: 12px;
  }
  .brand-dot {
    width: 18px; height: 18px;
    border-radius: 50%;
    background: var(--gold);
  }
  .brand-name {
    font-weight: 500;
    font-size: 32px;
    letter-spacing: 3px;
    color: var(--gold);
    text-transform: lowercase;
  }
  .title {
    position: absolute;
    top: 344px; left: 0; right: 0;
    text-align: center;
    font-weight: 700;
    font-size: 60px;
    letter-spacing: 2px;
    line-height: 72px;
    color: var(--white);
  }
  .presented {
    position: absolute;
    top: 420px; left: 0; right: 0;
    text-align: center;
    font-weight: 600;
    font-size: 18px;
    letter-spacing: 0.6px;
    color: var(--gold);
  }
  .recipient {
    position: absolute;
    top: 468px; left: 0; right: 0;
    text-align: center;
    font-family: "Kaushan Script", cursive;
    font-size: 72px;
    line-height: 96px;
    color: var(--white);
  }
  .recipient-rule {
    position: absolute;
    top: 570px; left: 264px;
    width: 730px; height: 1.5px;
    background: var(--white);
  }
  .citation {
    position: absolute;
    top: 604px; left: 0; right: 0;
    text-align: center;
    font-family: Arial, Helvetica, sans-serif;
    font-size: 16px;
    line-height: 20px;
    color: var(--white);
  }
  .sign-band {
    position: absolute;
    top: 670px; left: 22px; right: 22px;
    height: 134px;
    background: var(--band);
  }
  .sign-field { position: absolute; top: 102px; }
  .sign-field__line { height: 1.5px; background: var(--label); }
  .sign-field__label {
    margin-top: 7px;
    padding-left: 4px;
    font-weight: 500;
    font-size: 19px;
    line-height: 22px;
    color: var(--label);
  }
  .sign-field--date { left: 132px; width: 148px; }
  .sign-field--signature { left: 703px; width: 294px; }
  .sign-field--signature .sign-field__label { padding-left: 0; }
</style>
</head>
<body>
<main class="certificate">
  <div class="wave-texture" role="img" aria-label="Dark background with flowing diagonal wave lines"></div>
  <div class="gold-edge gold-edge--left"></div>
  <div class="gold-edge gold-edge--right"></div>

  <p class="cert-number">CERTIFICATE No. VG-0001</p>
  <p class="unit-count">1,000 UNITS</p>

  <div class="brand">
    <span class="brand-dot"></span>
    <span class="brand-name">Vantor Glide</span>
  </div>

  <h1 class="title">CERTIFICATE</h1>
  <p class="presented">THIS CERTIFICATE IS PROUDLY PRESENTED TO</p>
  <p class="recipient">Name Surname</p>
  <div class="recipient-rule"></div>
  <p class="citation">This certifies that the person named above is the registered owner of 1,000 fully paid Units of Vantor Glide,<br>transferable only on the books of the company in person or by duly authorized attorney.</p>

  <section class="sign-band">
    <div class="sign-field sign-field--date">
      <div class="sign-field__line"></div>
      <div class="sign-field__label">DATE</div>
    </div>
    <div class="sign-field sign-field--signature">
      <div class="sign-field__line"></div>
      <div class="sign-field__label">SIGNATURE</div>
    </div>
  </section>
</main>
</body>
</html>
```